Podcast Cover Art for Fast Growing Show (Ill include a gracious tip!)

This artwork is for "The Steadfast Fellow Show." The podcast is for men, and it's all about self-improvement, confidence, success, money, women and masculinity. It's for the guy who wants to improve himself. I'd like for my picture to be included — in black and white — and I want the text to read: "The Steadfast Fellow Show" and somewhere in there it'll say: "with Dale Prowen." I'm open to color schemes. The podcast is a little edgy so I'd like for that to be represented in the design. Thank you! (((Here's the podcast page if you wanna check it out: http://steadfastfellowshow.castorbit.net/)))

Target Market(s)

Men who want to attract women and improve their lives!

Font styles to use
Serif

Colors

Designer to choose colors to be used in the design.

Requirements
Must have
• My image in it (in black and white) and the two titles: "The Steadfast Fellow Show" and "with Dale Prowen"
Nice to have
• My logo in it somehow (which is the arrow looking logo attached below). I've also found that my image looks best in black and white and with a circular type cut out (although I'm open to different design ideas). I've attached my logo with a circular cut out below so you can see what I'm talking about.
Should not have
• Flowers. Teddy bears. ice cream.

```html
<!DOCTYPE html>
<html lang="en">
<head>
<meta charset="utf-8">
<title>The Steadfast Fellow Show — Cover Art</title>
<link href="https://fonts.googleapis.com/css2?family=Oswald:wght@500&family=Poppins:ital,wght@1,400&display=swap" rel="stylesheet">
<style>
  :root {
    --bg: #000000;
    --ink: #ffffff;
    --photo-light: #d9d6d2;
    --photo-dark: #3a3632;
  }
  html, body {
    margin: 0;
    padding: 0;
    width: 1200px;
    height: 1200px;
    overflow: hidden;
    background: var(--bg);
  }
  .cover {
    position: relative;
    width: 1200px;
    height: 1200px;
    background: var(--bg);
  }
  .cover-art {
    position: absolute;
    inset: 0;
    width: 1200px;
    height: 1200px;
  }
  .brand-name {
    font-family: "Oswald", sans-serif;
    font-weight: 500;
    font-size: 20px;
    letter-spacing: 4px;
    fill: var(--ink);
  }
  .show-title {
    font-family: "Oswald", sans-serif;
    font-weight: 500;
    font-size: 54px;
    letter-spacing: 3px;
    fill: var(--ink);
  }
  .frame-line {
    fill: none;
    stroke: var(--ink);
    stroke-width: 5;
    stroke-linecap: round;
  }
  .host-line {
    position: absolute;
    left: 0;
    right: 0;
    top: 900px;
    margin: 0;
    text-align: center;
    font-family: "Poppins", sans-serif;
    font-style: italic;
    font-weight: 400;
    font-size: 27px;
    color: var(--ink);
  }
</style>
</head>
<body>
  <main class="cover">
    <svg class="cover-art" viewBox="0 0 1200 1200" xmlns="http://www.w3.org/2000/svg">
      <defs>
        <radialGradient id="portrait-tone" cx="50%" cy="40%" r="60%">
          <stop offset="0%" stop-color="var(--photo-light)"/>
          <stop offset="55%" stop-color="#a8a39d"/>
          <stop offset="100%" stop-color="var(--photo-dark)"/>
        </radialGradient>
        <path id="title-arc" d="M381.4 686.5 A222 222 0 1 1 818.6 686.5"/>
      </defs>

      <text class="brand-name" x="600" y="310" text-anchor="middle">STEADFAST</text>

      <circle class="host-portrait" cx="600" cy="648" r="188" fill="url(#portrait-tone)"
              role="img" aria-label="Black and white portrait of host Dale Prowen, hands steepled under his chin"/>

      <text class="show-title" text-anchor="middle">
        <textPath href="#title-arc" startOffset="50%">THE STEADFAST FELLOW SHOW</textPath>
      </text>

      <path class="frame-line" d="M390.6 692 A214 214 0 0 0 809.4 692"/>
      <line class="frame-line" x1="352" y1="692" x2="374" y2="692"/>
      <line class="frame-line" x1="826" y1="692" x2="848" y2="692"/>
    </svg>

    <p class="host-line">with Dale Prowen</p>
  </main>
</body>
</html>
```